Brivo-Lent Online Pitch Deck Uplift

We are revamping our current Cloudmere TradeHub page listing by creating SIMPLE, BOLD, and APPEALING SLIDES to increase engagement on said page. For now, we would like you to work on the first THREE SLIDES (from Slides.pptx):

SLIDE 1
* Remove the hyphens from the title.
* Change subtitle wording to "Creates raving fans that inspires employees and accelerates business”
* Add a drop shadow to the four icons at the bottom to give the illusion of hovering over the slide. This feature should be applied to icons on the other two slides.
* Increase font size of the icon captions.

SLIDE 2
* For a general idea of the position of the elements on this slide, please see my rough sketch. See slide2_sketch.png under Uploaded Files for reference.
* For the "If you have" and "If you want" sections, please do them in the same style of the "If you have" and "If you want" sections in SLIDE 1 - but this time, the "If you have" part is placed on top of "If you want", connected by "Change it to" arrow in a downwards direction.
* On the left half of the slide, we would like you to recreate these screenshots - slide2_screenshot1.png, slide2_screenshot2.png - into vector. Then, arrange these screenshots like what's displayed on the homepage of www.zandorel.com.
* Use slide2_background.png as the slide background.
* Remove the icon caption "INTELLIGENT CUSTOMER FEEDBACK". This should also apply to similar slides
* You must only use the font Helvetica Neue Light for all slides.

SLIDE 3
* Redo the flowchart by making it isometric. (See slide3_isometric.png for reference.)
* Follow my sketch (i.e., slide3_sketch.png) to determine the proper order of elements.
* See the floating text on the left side of slide3_isometric.png? Add the following information to the slide and arrange them similar to the reference:
1. Multichannel surveys
2. AI categorised and live reports created
3. Feedback delivered to the right people (image of the web, etc.)

Industry/Entity Type

Software Service

Font styles to use
Other font styles liked:
• Helvetica Neue Light

Colors
0355a3
ffffff
f37122

Requirements
Should not have
• Red

```html
<!DOCTYPE html>
<html lang="en">
<head>
<meta charset="utf-8">
<title>Brivo-Lent Pitch Deck Board</title>
<link href="https://fonts.googleapis.com/css2?family=Roboto:wght@300;400&display=swap" rel="stylesheet">
<style>
:root{
  --blue:#0355a3;
  --blue-mid:#1f7cc4;
  --blue-light:#2d9be0;
  --orange:#f37122;
  --white:#ffffff;
  --ink:#222;
  --board-dark:#474747;
  --board-grey:#a9a9ab;
  --wood-a:#f0d3a0;
  --wood-b:#dcb27a;
  --panel-edge:#b9c8e6;
}
*{box-sizing:border-box;margin:0;padding:0}
html,body{width:1200px;height:1200px;overflow:hidden}
body{font-family:"Roboto",sans-serif;font-weight:300;color:var(--ink);position:relative;
  background:linear-gradient(90deg,var(--board-dark) 0 670px,var(--board-grey) 670px 1200px)}
.abs{position:absolute}
.slide{position:absolute;left:53px;width:570px;height:354px;overflow:hidden;box-shadow:0 6px 18px rgba(0,0,0,.45)}
.wood{background:linear-gradient(100deg,var(--wood-a),var(--wood-b) 45%,var(--wood-a) 70%,var(--wood-b))}
.s1{top:41px}.s2{top:424px}.s3{top:806px}
.s1-title{top:20px;width:100%;text-align:center;color:var(--blue-mid);font-size:26px}
.s1-sub{top:50px;width:100%;text-align:center;color:var(--blue-mid);font-size:14px}
.box{position:absolute;border-radius:12px;border:1.2px solid}
.box.have{border-color:var(--orange)}
.box.want{border-color:var(--blue-mid)}
.box h4{font-weight:300;text-align:center;font-size:12px;margin-top:14px}
.box.have h4{color:var(--orange)}
.box.want h4{color:var(--blue-mid)}
.box ul{list-style:none;font-size:8.2px;margin:6px 12px 0 12px;color:#222}
.box li{margin-bottom:5px;position:relative;padding-left:8px;line-height:1.15}
.box.have li::before{content:"×";color:var(--orange);position:absolute;left:0}
.box.want li::before{content:"✓";color:var(--blue-mid);position:absolute;left:0}
.mark{position:absolute;width:32px;height:32px;border-radius:50%;background:var(--white);border:2px solid}
.mark.x{border-color:var(--orange)}.mark.ok{border-color:var(--blue-mid)}
.mark svg{width:100%;height:100%}
.change-it{position:absolute;color:var(--white);font-size:10px}
.icon{position:absolute;width:74px;height:74px;border-radius:50%;
  background:radial-gradient(circle at 40% 35%,#fff,#e4e4e4 70%,#cfcfcf);
  box-shadow:0 8px 12px rgba(0,0,0,.3);display:flex;align-items:center;justify-content:center}
.icon svg{width:44px;height:44px}
.cap{position:absolute;width:96px;text-align:center;font-size:10px;color:#333;line-height:1.05}
.cap.small{width:76px;font-size:7.5px;color:#444}
.band{position:absolute;left:0;top:0;width:100%;height:70px;background:linear-gradient(180deg,#2a7fc8,var(--blue-mid))}
.band h2{color:var(--white);font-weight:300;font-size:21px;text-align:center;line-height:26px;padding:9px 0 0 80px}
.s2-body{position:absolute;left:0;top:70px;width:100%;height:284px;background:linear-gradient(120deg,#dfe8f1,#b9cad9 50%,#e3e9ef)}
.mini{position:absolute;background:var(--white);border:4px solid var(--panel-edge);box-shadow:0 4px 8px rgba(0,0,0,.2)}
.s2 .box{background:rgba(255,255,255,.25)}
.s3-art{position:absolute;left:127px;top:84px;width:380px;height:250px;border-radius:6px;
  background:linear-gradient(135deg,rgba(70,120,200,.35),rgba(190,170,220,.45) 55%,rgba(240,190,90,.45))}
.float{position:absolute;color:var(--blue);font-size:8.5px;line-height:1.05;transform:rotate(-30deg);transform-origin:left top;text-align:center}
.scene{left:670px;top:400px;width:530px;height:440px;background:linear-gradient(140deg,#c9b9dc,#b8b2c8 50%,#c7c3cc)}
.panel{position:absolute;background:var(--white);border:4px solid var(--panel-edge);box-shadow:0 6px 14px rgba(0,0,0,.3)}
.p-head{position:relative;height:50px;border-bottom:4px solid var(--panel-edge);background:var(--white)}
.burger{position:absolute;left:10px;top:10px;width:24px}
.burger i{display:block;height:2px;background:var(--blue-mid);margin-bottom:3px}
.p-title{position:absolute;left:10px;bottom:6px;color:var(--blue-mid);font-size:11px}
.edit{position:absolute;right:10px;top:16px;width:78px;height:22px;border:1px solid var(--blue-mid);border-radius:3px;color:var(--blue-mid);font-size:10px;display:flex}
.edit span{flex:1;display:flex;align-items:center;justify-content:center}
.edit b{width:26px;border-left:1px solid var(--blue-mid);display:flex;align-items:center;justify-content:center}
.card{position:relative;border-bottom:4px solid var(--panel-edge);padding:6px 8px;font-size:6px}
.card .link{color:var(--blue-mid);font-size:6px;position:absolute;left:8px;bottom:5px}
.disc table{width:100%;border-collapse:collapse;font-size:6.5px}
.disc th{font-weight:400;text-align:left;padding:8px 6px;border-bottom:4px solid var(--panel-edge)}
.disc td{padding:6px;border-bottom:1px solid #dde3ef}
.disc td.case{color:var(--blue-mid)}
</style>
</head>
<body>

<!-- Slide 1 -->
<section class="slide s1 wood">
  <h1 class="abs s1-title" style="font-weight:300">AI Driven – Feedback, Quality, &amp; Efficiency</h1>
  <p class="abs s1-sub">Creates Raving Fans That Inspires Employees &amp; Accelerates Business</p>
  <div class="box have" style="left:28px;top:102px;width:238px;height:108px">
    <h4>If you have</h4>
    <ul><li>Ineffective customer feedback</li><li>High repeat contact rates</li><li>Inconsistent quality of service</li><li>Team not engaged or learning fast enough</li></ul>
  </div>
  <div class="box want" style="left:293px;top:102px;width:252px;height:108px">
    <h4>If you want</h4>
    <ul><li>Fast intelligent customer feedback to each person/team</li><li>Solve customers issues first time</li><li>Consistent compliant audits in Cloudmere CRM</li><li>Motivated team regularly coached</li></ul>
  </div>
  <div class="mark x" style="left:126px;top:83px"><svg viewBox="0 0 32 32"><path d="M10 10l12 12M22 10L10 22" stroke="#f37122" stroke-width="2.5"/></svg></div>
  <div class="mark ok" style="left:400px;top:83px"><svg viewBox="0 0 32 32"><path d="M9 16l5 5 9-10" stroke="#1f7cc4" stroke-width="2.5" fill="none"/></svg></div>
  <svg class="abs" style="left:234px;top:108px" width="86" height="40" viewBox="0 0 86 40"><path d="M4 4h62V0l18 18-18 18v-4H8q-4 0-4 4z" fill="#1f7cc4"/></svg>
  <span class="change-it" style="left:248px;top:118px">Change it To</span>
  <div class="icon" style="left:92px;top:234px"><svg viewBox="0 0 44 44"><rect x="4" y="12" width="34" height="14" rx="4" fill="#fff" stroke="#1f7cc4"/><path d="M10 26l-2 6 7-6z" fill="#1f7cc4"/><g fill="#f37122"><circle cx="10" cy="19" r="2.3"/><circle cx="16" cy="19" r="2.3"/><circle cx="22" cy="19" r="2.3"/><circle cx="28" cy="19" r="2.3"/></g><path d="M33 10l7 2-7 3-7-3z" fill="#1f7cc4"/></svg></div>
  <div class="icon" style="left:192px;top:234px"><svg viewBox="0 0 44 44"><path d="M6 6v32h32" stroke="#0355a3" fill="none" stroke-width="1.5"/><path d="M10 32l8-8 6 4 12-14" stroke="#1f7cc4" fill="none" stroke-width="1.5"/><circle cx="16" cy="13" r="5" fill="#0355a3"/><circle cx="24" cy="13" r="3" fill="#f37122"/></svg></div>
  <div class="icon" style="left:294px;top:234px"><svg viewBox="0 0 44 44"><rect x="9" y="6" width="22" height="30" rx="2" fill="#0355a3"/><rect x="12" y="11" width="16" height="22" fill="#fff"/><path d="M15 16h10M15 21h10M15 26h8" stroke="#1f7cc4"/><circle cx="30" cy="22" r="6" fill="none" stroke="#f37122" stroke-width="2"/><path d="M34 26l5 5" stroke="#0355a3" stroke-width="2.5"/></svg></div>
  <div class="icon" style="left:394px;top:234px"><svg viewBox="0 0 44 44"><circle cx="24" cy="12" r="7" fill="#f37122"/><rect x="21" y="19" width="6" height="4" fill="#0355a3"/><rect x="12" y="28" width="20" height="10" rx="4" fill="#0355a3"/></svg></div>
  <p class="cap" style="left:81px;top:316px">Intelligent Customer Feedback</p>
  <p class="cap" style="left:181px;top:316px">Service Efficiency</p>
  <p class="cap" style="left:283px;top:316px">Quality and Auditing</p>
  <p class="cap" style="left:383px;top:316px">Team Engagement and Learning</p>
</section>

<!-- Slide 2 -->
<section class="slide s2">
  <div class="s2-body" role="img" aria-label="Soft blurred office photograph in pale blue tones"></div>
  <div class="band"><h2>Customer Feedback Automatically Categorized<br>and Used in Financials</h2></div>
  <div class="icon" style="left:20px;top:30px"><svg viewBox="0 0 44 44"><rect x="4" y="12" width="34" height="14" rx="4" fill="#fff" stroke="#1f7cc4"/><path d="M10 26l-2 6 7-6z" fill="#1f7cc4"/><g fill="#f37122"><circle cx="10" cy="19" r="2.3"/><circle cx="16" cy="19" r="2.3"/><circle cx="22" cy="19" r="2.3"/><circle cx="28" cy="19" r="2.3"/></g><path d="M33 10l7 2-7 3-7-3z" fill="#1f7cc4"/></svg></div>
  <div class="mini" style="left:30px;top:128px;width:170px;height:70px;transform:rotate(-10deg)">
    <div style="height:18px;border-bottom:2px solid var(--panel-edge)"></div>
    <div style="margin:5px;height:2px;background:#ccd"></div><div style="margin:5px;height:2px;background:#ccd"></div><div style="margin:5px;height:2px;background:#ccd"></div><div style="margin:5px;height:2px;background:#ccd"></div>
  </div>
  <div class="mini" style="left:125px;top:200px;width:120px;height:140px;transform:rotate(10deg)">
    <svg width="112" height="132" viewBox="0 0 112 132"><rect width="112" height="14" fill="#fff" stroke="#b9c8e6"/><path d="M40 48a18 18 0 0 1 36 0" stroke="#0355a3" stroke-width="3" fill="none"/><path d="M58 48l6-10" stroke="#222"/><text x="54" y="78" font-size="6">15</text><g fill="#1f7cc4"><rect x="12" y="112" width="8" height="6"/><rect x="24" y="110" width="8" height="8"/><rect x="36" y="108" width="8" height="10"/><rect x="48" y="107" width="8" height="11"/><rect x="60" y="109" width="8" height="9"/><rect x="72" y="108" width="8" height="10"/><rect x="84" y="96" width="8" height="22"/></g></svg>
  </div>
  <div class="box have" style="left:305px;top:94px;width:240px;height:110px">
    <h4 style="margin-top:20px">If you have</h4>
    <ul style="margin-top:8px;margin-right:26px"><li>No visibility of customer feedback by agent, process and client</li><li>Lack of action and accountability</li><li>No link to financial metrics to show the value of improvements</li></ul>
  </div>
  <div class="box want" style="left:303px;top:228px;width:242px;height:116px">
    <h4 style="margin-top:22px">If you want</h4>
    <ul style="margin-top:8px"><li>Automatic AI categorisation customer feedback by agent, process and client</li><li>Action through bringing relevant feedback to each individual</li><li>Realtime financial reports showing the loyalty value</li></ul>
  </div>
  <div class="mark x" style="left:408px;top:78px"><svg viewBox="0 0 32 32"><path d="M10 10l12 12M22 10L10 22" stroke="#f37122" stroke-width="2.5"/></svg></div>
  <div class="mark ok" style="left:410px;top:212px"><svg viewBox="0 0 32 32"><path d="M9 16l5 5 9-10" stroke="#1f7cc4" stroke-width="2.5" fill="none"/></svg></div>
  <svg class="abs" style="left:496px;top:176px" width="46" height="82" viewBox="0 0 46 82"><path d="M4 4q0-4 4-4h24v62h12L24 82 2 62h14V16H8q-4 0-4 4z" fill="#1f7cc4"/></svg>
  <span class="change-it" style="left:515px;top:182px;writing-mode:vertical-rl;transform:rotate(180deg)">Change it To</span>
</section>

<!-- Slide 3 -->
<section class="slide s3 wood">
  <div class="band"><h2>Feedback From All Channels Delivered To<br>Right Person</h2></div>
  <div class="icon" style="left:20px;top:30px"><svg viewBox="0 0 44 44"><rect x="4" y="12" width="34" height="14" rx="4" fill="#fff" stroke="#1f7cc4"/><path d="M10 26l-2 6 7-6z" fill="#1f7cc4"/><g fill="#f37122"><circle cx="10" cy="19" r="2.3"/><circle cx="16" cy="19" r="2.3"/><circle cx="22" cy="19" r="2.3"/><circle cx="28" cy="19" r="2.3"/></g><path d="M33 10l7 2-7 3-7-3z" fill="#1f7cc4"/></svg></div>
  <div class="s3-art" role="img" aria-label="Isometric flow: phone survey, AI assistant, report screen, and team members receiving feedback beside a money bag"></div>
  <p class="float" style="left:128px;top:202px">Multichannel<br>survey</p>
  <p class="float" style="left:205px;top:148px">AI categorised and<br>live reports created</p>
  <p class="float" style="left:282px;top:110px">Feedback delivered<br>to the right people</p>
</section>

<!-- Isometric scene -->
<div class="abs scene" role="img" aria-label="Isometric board: tablet showing celebrate and save, team members holding process, price, support and web cards, and a money bag on a pedestal"></div>

<!-- Report panel -->
<div class="panel" style="left:764px;top:30px;width:268px;height:366px;background:#eef2f9">
  <div class="p-head" style="height:48px"><div class="burger"><i></i><i></i><i></i></div><span class="p-title">REPORT</span><div class="edit"><span>EDIT</span><b>▼</b></div></div>
  <div class="card" style="height:116px;background:#fff">Personal NPS Last 30 days
    <svg class="abs" style="left:74px;top:18px" width="116" height="80" viewBox="0 0 116 80"><path d="M8 66a50 50 0 0 1 100 0" stroke="#22336b" stroke-width="5" fill="none"/><path d="M75 20a50 50 0 0 1 33 46" stroke="#2d9be0" stroke-width="5" fill="none"/><path d="M94 32a50 50 0 0 1 14 34" stroke="#1a6d78" stroke-width="5" fill="none"/><path d="M50 66l18-30-12 32z" fill="#222"/><text x="52" y="78" font-size="9" fill="#f37122">40</text></svg>
    <span class="link">View Report</span></div>
  <div class="card" style="height:58px;background:#fff">NPS surveys completed<span class="abs" style="left:124px;top:22px;font-size:14px">15</span><span class="link">View Report</span></div>
  <div class="card" style="height:136px;background:#fff;border-bottom:0">NPS Score by Month
    <svg class="abs" style="left:8px;top:16px" width="250" height="112" viewBox="0 0 250 112"><path d="M14 4v58h226M14 30h226" stroke="#ccc" stroke-width=".6" fill="none"/><g fill="#1f7cc4"><rect x="20" y="48" width="22" height="14"/><rect x="50" y="44" width="22" height="18"/><rect x="80" y="40" width="22" height="22"/><rect x="110" y="35" width="22" height="27"/><rect x="140" y="41" width="22" height="21"/><rect x="170" y="38" width="22" height="24"/><rect x="200" y="6" width="22" height="56"/></g><g font-size="4.5" fill="#333"><text x="14" y="84" transform="rotate(-40 14 84)">January 2016</text><text x="46" y="84" transform="rotate(-40 46 84)">February 2016</text><text x="78" y="84" transform="rotate(-40 78 84)">March 2016</text><text x="108" y="84" transform="rotate(-40 108 84)">April 2016</text><text x="138" y="84" transform="rotate(-40 138 84)">May 2016</text><text x="168" y="84" transform="rotate(-40 168 84)">June 2016</text><text x="196" y="84" transform="rotate(-40 196 84)">September 2016</text><text x="226" y="84" transform="rotate(-40 226 84)">October 2016</text><text x="106" y="102">Completed Date</text></g></svg>
    <span class="link">View Report</span></div>
</div>

<!-- Icon row -->
<div class="icon" style="left:860px;top:868px;width:60px;height:60px"><svg viewBox="0 0 44 44"><rect x="4" y="12" width="34" height="14" rx="4" fill="#fff" stroke="#1f7cc4"/><g fill="#f37122"><circle cx="10" cy="19" r="2.3"/><circle cx="16" cy="19" r="2.3"/><circle cx="22" cy="19" r="2.3"/><circle cx="28" cy="19" r="2.3"/></g></svg></div>
<div class="icon" style="left:938px;top:868px;width:60px;height:60px"><svg viewBox="0 0 44 44"><path d="M6 6v32h32" stroke="#0355a3" fill="none" stroke-width="1.5"/><path d="M10 32l8-8 6 4 12-14" stroke="#1f7cc4" fill="none" stroke-width="1.5"/><circle cx="16" cy="13" r="5" fill="#0355a3"/></svg></div>
<div class="icon" style="left:1018px;top:868px;width:60px;height:60px"><svg viewBox="0 0 44 44"><rect x="9" y="6" width="22" height="30" rx="2" fill="#0355a3"/><rect x="12" y="11" width="16" height="22" fill="#fff"/><circle cx="30" cy="22" r="6" fill="none" stroke="#f37122" stroke-width="2"/></svg></div>
<div class="icon" style="left:1097px;top:868px;width:60px;height:60px"><svg viewBox="0 0 44 44"><circle cx="24" cy="12" r="7" fill="#f37122"/><rect x="12" y="28" width="20" height="10" rx="4" fill="#0355a3"/></svg></div>
<p class="cap small" style="left:852px;top:934px">Intelligent Customer Feedback</p>
<p class="cap small" style="left:930px;top:934px">Service Efficiency</p>
<p class="cap small" style="left:1010px;top:934px">Quality and Auditing</p>
<p class="cap small" style="left:1089px;top:934px">Team Engagement and Learning</p>

<!-- Discovery panel -->
<div class="panel disc" style="left:764px;top:980px;width:368px;height:178px">
  <div class="p-head" style="height:64px"><div class="burger" style="top:14px;width:34px"><i></i><i></i><i></i></div><span class="p-title" style="font-size:14px">Discovery</span><div class="edit" style="width:106px;height:30px;font-size:13px"><span>EDIT</span><b style="width:36px">▼</b></div></div>
  <table>
    <tr><th>EMPLOYEE</th><th>CASE</th><th>LOYALTY</th><th>NPS</th><th>FEEDBACK COMMENT</th></tr>
    <tr><td>Agent 1</td><td class="case">00102827</td><td>1</td><td>1</td><td>The website is not very intuitive, and the service agents were ..</td></tr>
    <tr><td>Agent 1</td><td class="case">00102806</td><td>10</td><td>10</td><td>your website is amazing, love the service agent too</td></tr>
    <tr><td>Agent 1</td><td class="case">00102765</td><td>10</td><td>10</td><td>Love the help</td></tr>
    <tr><td>Agent 1</td><td class="case">00102765</td><td>4</td><td>4</td><td>SO SLOW, why does it take so long</td></tr>
  </table>
</div>

</body>
</html>
```